mothers day ad for martial arts school

I am looking to have a nice flyer/handout to promote my martial arts school. It is for our promotion of "mom's train free" for mothers day in May. I would like an ad that would inspire a mother to learn self defense and to improve their fitness. It can have pictures but not necessarily a requirement. Pictures don't have to be of a lady in a martial arts uniform. It may be better if they are not. It also doesn't have to be standard sheet of paper size, as these are going to be handouts the size can be smaller. I would like our Copper Vale logo on the flyer.

Target Market(s)

mothers that hadn't thought about martial arts before but would be convinced to try it

Industry/Entity Type

School

Requirements
Must have
• text, photos that would appeal to and encourage a mother to try a self defense/fitness class
Nice to have
• our logo and text and possibly pictures that would inspire a mother to join a martial arts class

```html
<!DOCTYPE html>
<html lang="en">
<head>
<meta charset="utf-8">
<title>Moms Train Free – Copper Vale Martial Arts</title>
<link rel="stylesheet" href="https://fonts.googleapis.com/css2?family=Kaushan+Script&family=Oswald:wght@300;400;600&display=swap">
<style>
  :root {
    --paper: #f3efea;
    --paper-shade: #e4ddd6;
    --belt-pink: #e9c3b4;
    --rose: #9e2a3a;
    --ink: #141414;
    --accent-red: #d3202f;
  }
  html, body {
    margin: 0;
    padding: 0;
    width: 846px;
    height: 1200px;
    overflow: hidden;
    background: var(--paper);
  }
  .flyer {
    position: relative;
    width: 846px;
    height: 1200px;
    overflow: hidden;
    font-family: "Oswald", "Arial Narrow", sans-serif;
    color: var(--ink);
  }
  .flyer__photo {
    position: absolute;
    inset: 0;
    background:
      radial-gradient(ellipse 120px 110px at 100px 30px, rgba(158,42,58,0.55), transparent 70%),
      radial-gradient(ellipse 110px 120px at 40px 270px, rgba(158,42,58,0.5), transparent 70%),
      radial-gradient(ellipse 110px 120px at 800px 770px, rgba(158,42,58,0.5), transparent 70%),
      radial-gradient(ellipse 380px 520px at 470px 500px, rgba(233,195,180,0.55), transparent 75%),
      linear-gradient(160deg, var(--paper) 0%, #f7f4f0 45%, var(--paper-shade) 100%);
  }
  .headline {
    position: absolute;
    left: 0;
    width: 100%;
    margin: 0;
    text-align: center;
    font-family: "Kaushan Script", cursive;
    font-weight: 400;
    line-height: 1;
    color: var(--ink);
  }
  .headline__line {
    position: absolute;
    left: 0;
    width: 100%;
    font-size: 190px;
  }
  .headline__line--moms  { top: 110px; }
  .headline__line--train { top: 320px; }
  .headline__line--free  { top: 480px; }
  .offer {
    position: absolute;
    top: 750px;
    left: 0;
    width: 100%;
    text-align: center;
  }
  .offer__title {
    margin: 0;
    font-weight: 300;
    font-size: 42px;
    line-height: 1;
  }
  .offer__note {
    margin: 10px 0 0;
    font-weight: 300;
    font-size: 22px;
    letter-spacing: 0.2px;
  }
  .brand {
    position: absolute;
    top: 930px;
    left: 0;
    width: 100%;
    display: flex;
    justify-content: center;
    align-items: center;
    gap: 18px;
  }
  .brand__mark {
    width: 52px;
    height: 52px;
    background: var(--accent-red);
  }
  .brand__name {
    font-weight: 600;
    font-size: 50px;
    line-height: 1;
    letter-spacing: 1px;
    text-transform: uppercase;
    color: var(--ink);
  }
  .contact {
    position: absolute;
    top: 1022px;
    left: 0;
    width: 100%;
    text-align: center;
  }
  .contact__phone {
    margin: 0;
    font-weight: 600;
    font-size: 40px;
    color: var(--accent-red);
    letter-spacing: 1px;
  }
  .contact__address {
    margin: 22px 0 0;
    font-weight: 400;
    font-size: 21px;
    text-transform: uppercase;
  }
</style>
</head>
<body>
  <main class="flyer">
    <div class="flyer__photo" role="img" aria-label="Pale pink martial arts belt curling down the page like a ribbon, with scattered red roses on a pale stone surface"></div>

    <h1 class="headline">
      <span class="headline__line headline__line--moms">Moms</span>
      <span class="headline__line headline__line--train">Train</span>
      <span class="headline__line headline__line--free">Free</span>
    </h1>

    <section class="offer">
      <p class="offer__title">All Month Long</p>
      <p class="offer__note">To honor all Mother's in the month of May</p>
    </section>

    <div class="brand">
      <span class="brand__mark"></span>
      <span class="brand__name">Copper Vale Martial Arts</span>
    </div>

    <section class="contact">
      <p class="contact__phone">(555) 214-7730</p>
      <p class="contact__address">2870 W Maple Ridge Rd Fairbrook, KS 60000</p>
    </section>
  </main>
</body>
</html>
```